Verdant Holdings Scholarship

Looking to make an attractive scholarship description graphic for my website. Please use the text on the word doc and integrate the two graphics into the layout. Here's what I am looking to replace with the winning design: https://qmeadowllc.example/scholarship-contest/

Thank you

```html
<!DOCTYPE html>
<html lang="en">
<head>
<meta charset="utf-8">
<title>Verdant Holdings High School Scholarship</title>
<link rel="stylesheet" href="https://fonts.googleapis.com/css2?family=Roboto:wght@300;400;500;700&display=swap">
<style>
  :root {
    --purple: #500a7d;
    --gold: #d2b604;
    --gold-deep: #c9a40e;
    --lavender: #e8e8fb;
    --panel: #e1e1e1;
    --text: #555555;
    --white: #ffffff;
    --teal: #1f3b3a;
    --olive: #8c9b58;
  }
  * { margin: 0; padding: 0; box-sizing: border-box; }
  html, body { width: 878px; height: 1200px; overflow: hidden; background: var(--white); }
  body { font-family: "Roboto", Arial, sans-serif; color: var(--text); }
  .canvas { position: relative; width: 878px; height: 1200px; overflow: hidden; }

  .hero { position: absolute; left: 0; top: 0; width: 878px; height: 342px; background: var(--lavender); }
  .brand { position: absolute; left: 80px; top: 218px; display: flex; align-items: center; gap: 10px; }
  .brand-mark { width: 22px; height: 22px; background: var(--gold); }
  .brand-name { font-family: "Roboto", Arial, sans-serif; font-weight: 700; font-size: 30px; color: var(--purple); letter-spacing: -0.3px; }
  .hero-art { position: absolute; left: 412px; top: 92px; width: 418px; height: 250px;
    background: linear-gradient(160deg, #ddd9f4 0%, #d8c872 55%, #8c9b58 100%); border-radius: 6px 6px 0 0; }

  .side-panel { position: absolute; left: 502px; top: 465px; width: 376px; height: 598px; background: var(--panel); }

  .icon { position: absolute; border-radius: 6px; }
  .icon-target { left: 67px; top: 385px; width: 90px; height: 90px; border-radius: 50%;
    background: radial-gradient(circle, var(--gold) 0 10%, var(--teal) 10% 30%, var(--white) 30% 42%, var(--purple) 42% 78%, #ececec 78%); }
  .icon-checklist { left: 68px; top: 570px; width: 80px; height: 93px; background: linear-gradient(135deg, var(--gold) 0 70%, #d9d9d9 70%); }
  .icon-monitor { left: 68px; top: 826px; width: 85px; height: 82px; background: linear-gradient(180deg, var(--gold) 0 70%, var(--purple) 70%); }

  .section { position: absolute; }
  .section-left { left: 178px; width: 270px; }
  .section-right { left: 569px; width: 262px; }

  .heading { font-weight: 700; font-size: 16.4px; line-height: 20.7px; color: var(--purple); letter-spacing: 0.1px; text-transform: uppercase; }
  .copy { font-weight: 300; font-size: 9.2px; line-height: 17.4px; letter-spacing: 0.15px; }
  .copy strong { font-weight: 500; color: var(--purple); }
  .copy-loose { line-height: 20.2px; }

  .bullets { list-style: none; }
  .bullets li { position: relative; padding-left: 16px; font-weight: 300; font-size: 9.2px; line-height: 17.4px; letter-spacing: 0.15px; margin-bottom: 11.8px; }
  .bullets li::before { content: "•"; position: absolute; left: 0; top: 0; font-size: 6px; }
  .bullets li:last-child { margin-bottom: 0; }

  .notice { font-weight: 500; color: var(--purple); }
</style>
</head>
<body>
<main class="canvas">
  <header class="hero">
    <div class="brand">
      <span class="brand-mark"></span>
      <span class="brand-name">Verdant Holdings</span>
    </div>
    <div class="hero-art" role="img" aria-label="Illustration of a school building with a flag, graduation cap, diploma, stacked books and three students"></div>
  </header>

  <div class="side-panel"></div>

  <div class="icon icon-target" role="img" aria-label="Target with an arrow in the bullseye"></div>
  <div class="icon icon-checklist" role="img" aria-label="Checklist document with a magnifying glass"></div>
  <div class="icon icon-monitor" role="img" aria-label="Computer monitor showing an application form"></div>

  <section class="section section-left" style="top:382px">
    <h2 class="heading">Purpose of this scholarship:</h2>
    <ul class="bullets" style="margin-top:5px">
      <li>To increase trade school, college, and university opportunities of high school seniors</li>
      <li>To encourage high academic achievement in our youth</li>
      <li>To reward hard-working high school seniors and assist in collegiate expenses</li>
    </ul>
  </section>

  <section class="section section-left" style="top:554px">
    <h2 class="heading">Eligibility and requirements at the time of submission for this scholarship:</h2>
    <ul class="bullets" style="margin-top:12px">
      <li>Applicant must be an enrolled high school student in his/her senior year</li>
      <li>Applicant must be in good standing with their high school</li>
      <li>Applicant must have a cumulative grade point average of at least 2.5 on a 4.0 scale</li>
      <li>Applicant must be accepted to a 4-year accredited college, university, trade school or community college</li>
    </ul>
  </section>

  <section class="section section-left" style="top:827px">
    <h2 class="heading">Application:</h2>
    <p class="copy" style="margin-top:5px">The application can be submitted via upload on this website, mail (see mailing address below), or scan &amp; email. Email address: <strong>ellenmeadow@qmeadowllc.example.</strong> The Application package must include:</p>
    <ul class="bullets" style="margin-top:12px">
      <li>Completed application form</li>
      <li>1 completed scholarship recommendation (teacher, guidance counselor, coach, employer, clergy, NOT friends or family)</li>
      <li>1 Essay no more than 2 pages in length, Times New Roman font (size 12), 1” margins, &amp; double-spaced</li>
      <li>Current high school transcript</li>
      <li>A copy of a College, University, Trade School or Community College acceptance letter</li>
    </ul>
  </section>

  <section class="section section-right" style="top:523px">
    <h2 class="heading">Scoring:</h2>
    <p class="copy" style="margin-top:5px">The Verdant Holdings Scholarship Scoring Committee will evaluate each application and select ONE winner. If there is a tie, the prize money will be split. The winning essay will be scored based on the grading rubric (Rubric is in downloadable scholarship application packet).</p>
  </section>

  <section class="section section-right" style="top:686px">
    <h2 class="heading">Scholarship amount:</h2>
    <p class="copy copy-loose" style="margin-top:3px">The Verdant Holdings Scholarship will award a minimum of <strong>$1,500.00</strong> to the winning applicant. Payment will be to the institution that the winner will attend in the fall.</p>
  </section>

  <section class="section section-right" style="top:817px">
    <h2 class="heading">Deadline:</h2>
    <p class="copy copy-loose" style="margin-top:3px"><span class="notice">The contest begins on 1 March. Applications postmarked, uploaded, and emailed after 31 May will not be accepted</span> and returned to sender. Verdant Holdings will announce the winner no later than 1 August.</p>
  </section>

  <section class="section section-right" style="top:948px">
    <h2 class="heading">Essay topic:</h2>
    <p class="copy" style="margin-top:4px;padding-left:3px">The essay topic is posted on the last day of February</p>
  </section>
</main>
</body>
</html>
```